I need business cards for a company that will be an umbrella for many retail stores. I need them to be sleek and modern. I would like some white and black in the background of the card as these are the office colours the logo is attached.
Target Market(s)
worldwide
Industry/Entity Type
Business
Requirements
Must have
- traditional business card shape
Should not have
- too many colours
no swirly text

```html
<!DOCTYPE html>
<html lang="en">
<head>
<meta charset="utf-8">
<title>Norva General Trading – Business Cards</title>
<link rel="stylesheet" href="https://fonts.googleapis.com/css2?family=Cinzel:wght@500;700&family=Arimo:wght@700&display=swap">
<style>
  :root {
    --canvas: #e9e7e4;
    --ink: #1c1c1c;
    --black-band: #232323;
    --silver-light: #f4f4f4;
    --silver-mid: #c9c9c9;
    --silver-dark: #7c7c7c;
    --brand-blue: #2f6db5;
    --pale-blue: #a9c2e6;
    --white: #ffffff;
  }
  html, body {
    margin: 0;
    width: 1200px;
    height: 900px;
    overflow: hidden;
    background: var(--canvas);
  }
  .sheet {
    position: relative;
    width: 1200px;
    height: 900px;
  }
  .card {
    position: absolute;
    left: 34px;
    width: 390px;
    height: 218px;
    box-shadow: 0 2px 6px rgba(0,0,0,.25);
  }
  .card--front-silver { top: 76px; }
  .card--front-band { top: 334px; }
  .card--back { top: 587px; }
  .card svg { display: block; }

  .side-label {
    position: absolute;
    margin: 0;
    font: 700 25px "Arimo", sans-serif;
    letter-spacing: 2px;
    color: var(--ink);
  }
  .side-label--one { left: 442px; top: 178px; }
  .side-label--two { left: 447px; top: 428px; }
  .side-label--three { left: 445px; top: 652px; }

  .brand-name { font-family: "Cinzel", serif; font-weight: 500; fill: var(--ink); }
  .holder-name { font-family: "Cinzel", serif; font-weight: 700; font-size: 10px; fill: var(--ink); letter-spacing: .5px; }
  .holder-title { font-family: "Arimo", sans-serif; font-weight: 700; font-size: 11px; fill: var(--brand-blue); letter-spacing: 1px; }
  .contact-heading { font-family: "Arimo", sans-serif; font-weight: 700; font-size: 8px; fill: var(--ink); letter-spacing: .6px; }
  .contact-heading--light { fill: var(--white); }
  .contact-line { font-family: "Arimo", sans-serif; font-weight: 700; font-size: 8px; fill: var(--brand-blue); letter-spacing: .6px; }
  .brand-dot { fill: var(--brand-blue); }
</style>
</head>
<body>
<main class="sheet">

  <!-- Front, silver sweep version -->
  <div class="card card--front-silver">
    <svg width="390" height="218" viewBox="0 0 390 218">
      <defs>
        <linearGradient id="silverBase" x1="0" y1="0" x2="1" y2="0">
          <stop offset="0" stop-color="#8d8d8d"/>
          <stop offset=".45" stop-color="#e2e2e2"/>
          <stop offset="1" stop-color="#f6f6f6"/>
        </linearGradient>
        <linearGradient id="sweepBand" x1="0" y1="0" x2="1" y2="0">
          <stop offset="0" stop-color="#9a9a9a"/>
          <stop offset="1" stop-color="#f2f2f2"/>
        </linearGradient>
        <linearGradient id="rule" x1="0" y1="0" x2="0" y2="1">
          <stop offset="0" stop-color="#ffffff"/>
          <stop offset="1" stop-color="#2f6db5"/>
        </linearGradient>
      </defs>
      <rect width="390" height="218" fill="url(#silverBase)"/>
      <path d="M70 0 H130 Q60 90 78 218 H20 Q20 90 70 0Z" fill="url(#sweepBand)" opacity=".8"/>
      <path d="M150 0 H215 Q135 100 160 218 H100 Q95 90 150 0Z" fill="url(#sweepBand)" opacity=".7"/>
      <path d="M235 0 H300 Q220 110 245 218 H185 Q180 95 235 0Z" fill="url(#sweepBand)" opacity=".6"/>
      <rect x="218" y="8" width="3" height="168" fill="url(#rule)"/>
      <g fill="var(--brand-blue)">
        <rect x="217" y="180" width="5" height="3"/>
        <rect x="217" y="186" width="5" height="3"/>
        <rect x="217" y="192" width="5" height="3"/>
        <rect x="217" y="198" width="5" height="3"/>
        <rect x="217" y="204" width="5" height="3"/>
      </g>
      <circle class="brand-dot" cx="24" cy="44" r="9"/>
      <text class="brand-name" x="42" y="40" font-size="19">Norva</text>
      <text class="brand-name" x="42" y="58" font-size="13">General Trading</text>
      <text class="holder-name" x="114" y="180" text-anchor="middle">Card Holder's Name</text>
      <text class="holder-title" x="114" y="193" text-anchor="middle">Title</text>
      <text class="contact-heading" x="229" y="138">Main Address:</text>
      <text class="contact-line" x="229" y="149">Tel:</text>
      <text class="contact-line" x="229" y="160">Mob:</text>
      <text class="contact-line" x="229" y="171">Fax:</text>
      <text class="contact-line" x="229" y="182">Email:</text>
      <text class="contact-line" x="229" y="193">Website:</text>
    </svg>
  </div>
  <p class="side-label side-label--one">Front</p>

  <!-- Front, black band version -->
  <div class="card card--front-band">
    <svg width="390" height="218" viewBox="0 0 390 218">
      <defs>
        <linearGradient id="bandBack" x1="0" y1="0" x2="1" y2="0">
          <stop offset="0" stop-color="#dcdcdc"/>
          <stop offset="1" stop-color="#9d9d9d"/>
        </linearGradient>
        <linearGradient id="panelFace" x1="0" y1="0" x2="0" y2="1">
          <stop offset="0" stop-color="#d4d4d4"/>
          <stop offset=".45" stop-color="#ffffff"/>
          <stop offset="1" stop-color="#ffffff"/>
        </linearGradient>
      </defs>
      <rect width="390" height="218" fill="url(#bandBack)"/>
      <rect y="154" width="390" height="64" fill="var(--black-band)"/>
      <path d="M0 0 H370 V128 Q370 154 344 154 H0Z" fill="url(#panelFace)"/>
      <path d="M366 0 H372 V128 Q372 156 344 156 H0 V152 H344 Q366 152 366 128Z" fill="#8a8a8a"/>
      <circle class="brand-dot" cx="24" cy="44" r="9"/>
      <text class="brand-name" x="42" y="40" font-size="19">Norva</text>
      <text class="brand-name" x="42" y="58" font-size="13">General Trading</text>
      <text class="holder-name" x="176" y="108" text-anchor="middle">Card Holder's Name</text>
      <text class="holder-title" x="176" y="121" text-anchor="middle">Title</text>
      <text class="contact-heading contact-heading--light" x="185" y="164">Main Address:</text>
      <text class="contact-line" x="185" y="175">Tel:</text>
      <text class="contact-line" x="185" y="185">Mob:</text>
      <text class="contact-line" x="185" y="195">Fax:</text>
      <text class="contact-line" x="185" y="205">Email:</text>
      <text class="contact-line" x="185" y="215">Website:</text>
    </svg>
  </div>
  <p class="side-label side-label--two">Front</p>

  <!-- Back -->
  <div class="card card--back">
    <svg width="390" height="218" viewBox="0 0 390 218">
      <defs>
        <linearGradient id="darkSweep" x1="0" y1="0" x2="1" y2="0">
          <stop offset="0" stop-color="#1f1f1f"/>
          <stop offset=".55" stop-color="#6f6f6f"/>
          <stop offset="1" stop-color="#d9d9d9"/>
        </linearGradient>
        <linearGradient id="blueRule" x1="0" y1="0" x2="1" y2="0">
          <stop offset="0" stop-color="#ffffff" stop-opacity="0"/>
          <stop offset=".5" stop-color="#a9c2e6"/>
          <stop offset="1" stop-color="#2f6db5"/>
        </linearGradient>
      </defs>
      <rect width="390" height="218" fill="#efefef"/>
      <path d="M0 0 H275 Q160 70 140 218 H0Z" fill="url(#darkSweep)"/>
      <path d="M275 0 H300 Q175 80 165 218 H140 Q160 70 275 0Z" fill="#d0d0d0" opacity=".7"/>
      <rect x="130" y="146" width="260" height="3" fill="url(#blueRule)"/>
      <circle class="brand-dot" cx="150" cy="100" r="10"/>
      <text class="brand-name" x="168" y="112" font-size="24">Norva</text>
      <text class="brand-name" x="168" y="138" font-size="17">General Trading</text>
    </svg>
  </div>
  <p class="side-label side-label--three">Back</p>

</main>
</body>
</html>
```